the ridgewell craft premier branch

design a DL A4 tri fold brochure to reflect our creative landscape business
my web site www.theridgewellcraft.com.au
has all the information needed
i will also be updating the website to be more updated and creative design

```html
<!DOCTYPE html>
<html lang="en">
<head>
<meta charset="utf-8">
<title>The Ridgewell Craft – Landscape Consulting and Design</title>
<link rel="stylesheet" href="https://fonts.googleapis.com/css2?family=Open+Sans:wght@400;600;700&family=Oswald:wght@500&display=swap">
<style>
  :root {
    --green: #6cb52d;
    --green-light: #9bd04a;
    --green-dark: #4f9a1f;
    --paper: #f2f2f2;
    --text: #3b3b3b;
    --rule: #c9c9c9;
    --white: #ffffff;
    --foliage-a: #5b7a3a;
    --foliage-b: #2f4a2a;
    --deck-a: #3a2b22;
    --deck-b: #8a5a35;
  }
  * { box-sizing: border-box; margin: 0; padding: 0; }
  html, body { width: 1200px; height: 855px; overflow: hidden; background: var(--white); }
  .brochure {
    position: relative; width: 1200px; height: 855px; overflow: hidden;
    background: var(--paper); font-family: "Open Sans", Arial, sans-serif; color: var(--text);
  }
  .layer { position: absolute; left: 0; top: 0; }

  /* Left panel */
  .intro { position: absolute; left: 35px; top: 62px; width: 340px; color: var(--white); }
  .intro__title { font-size: 19px; font-weight: 700; text-align: center; letter-spacing: .1px; }
  .intro__subtitle { font-size: 14.5px; font-weight: 600; text-align: center; margin-top: 6px; margin-bottom: 20px; }
  .intro p { font-size: 13.6px; line-height: 18.4px; text-align: justify; margin-bottom: 18px; }

  /* Services */
  .service { position: absolute; left: 438px; width: 340px; }
  .service__head { display: flex; align-items: center; gap: 12px; height: 46px; }
  .service__icon { width: 46px; height: 46px; flex: none; }
  .service__title { font-size: 17px; font-weight: 400; color: #222; letter-spacing: .2px; }
  .service__list { list-style: none; margin-top: 6px; margin-left: 2px; }
  .service__list li { display: flex; align-items: center; gap: 13px; font-size: 14.5px; height: 28px; }
  .bullet { width: 14px; height: 14px; flex: none; }

  /* Process */
  .process { position: absolute; left: 813px; top: 364px; width: 340px; }
  .process__title { font-size: 17px; color: #222; margin-bottom: 12px; letter-spacing: .2px; }
  .process__step { display: flex; gap: 10px; padding: 7px 0 10px; border-bottom: 1px dashed var(--rule); }
  .process__step:last-child { border-bottom: none; }
  .process__step p { font-size: 13.8px; line-height: 18.4px; text-align: justify; }
  .tick { width: 15px; height: 15px; flex: none; margin-top: 2px; }

  /* Footer brand */
  .brand { position: absolute; right: 30px; top: 752px; text-align: right; color: var(--white); }
  .brand__name { font-size: 22px; font-weight: 700; letter-spacing: -.2px; line-height: 1; }
  .brand__division { font-size: 9px; letter-spacing: 4px; margin-top: 4px; margin-right: 4px; }
  .callout { position: absolute; right: 30px; top: 804px; display: flex; align-items: center; gap: 8px;
    font-family: "Oswald", "Arial Narrow", sans-serif; font-weight: 500; font-size: 23px; color: var(--white); }
  .callout svg { width: 22px; height: 22px; }
</style>
</head>
<body>
<main class="brochure">

  <!-- Panel shapes -->
  <svg class="layer" width="1200" height="855" viewBox="0 0 1200 855" aria-hidden="true">
    <defs>
      <linearGradient id="panelGreen" x1="0" y1="0" x2="0" y2="1">
        <stop offset="0" stop-color="#5fae24"/>
        <stop offset=".6" stop-color="#79bd35"/>
        <stop offset="1" stop-color="#b9dc7c"/>
      </linearGradient>
      <linearGradient id="footerGreen" x1="0" y1="0" x2="1" y2="0">
        <stop offset="0" stop-color="#8cc63f"/>
        <stop offset="1" stop-color="#5fae24"/>
      </linearGradient>
    </defs>
    <path d="M0 0H405V455Q200 440 0 482Z" fill="url(#panelGreen)"/>
    <path d="M0 478Q200 446 405 456V470Q200 458 0 492Z" fill="#e4e4e4"/>
    <path d="M405 318Q640 352 880 340Q1060 330 1200 282V298Q1060 348 880 356Q640 366 405 334Z" fill="#dcdcdc"/>
    <path d="M760 855Q980 748 1200 712V855Z" fill="#d4d4d4"/>
    <path d="M780 855Q1000 760 1200 724V855Z" fill="url(#footerGreen)"/>
  </svg>

  <!-- Photo areas -->
  <svg class="layer" width="1200" height="855" viewBox="0 0 1200 855" role="img" aria-label="Photo of a lush planted garden with purple flowers and a stepping path">
    <defs>
      <linearGradient id="gardenTones" x1="0" y1="0" x2="1" y2="1">
        <stop offset="0" stop-color="#4e6d33"/>
        <stop offset=".5" stop-color="#6f8f4a"/>
        <stop offset="1" stop-color="#3f5a30"/>
      </linearGradient>
    </defs>
    <path d="M405 0H1200V280Q1060 328 880 336Q640 346 405 314Z" fill="url(#gardenTones)"/>
  </svg>
  <svg class="layer" width="1200" height="855" viewBox="0 0 1200 855" role="img" aria-label="Photo of a timber deck with outdoor dining setting under a lit pergola">
    <defs>
      <linearGradient id="deckTones" x1="0" y1="0" x2="0" y2="1">
        <stop offset="0" stop-color="#2c3550"/>
        <stop offset=".55" stop-color="#4a3a30"/>
        <stop offset="1" stop-color="#9a6a40"/>
      </linearGradient>
    </defs>
    <path d="M0 492Q200 460 405 470V855H0Z" fill="url(#deckTones)"/>
  </svg>
  <svg class="layer" width="1200" height="855" viewBox="0 0 1200 855" role="img" aria-label="Round photo of a timber deck beside a lawn">
    <circle cx="921" cy="248" r="75" fill="#ffffff"/>
    <circle cx="921" cy="248" r="70" fill="#6f7f5a"/>
  </svg>
  <svg class="layer" width="1200" height="855" viewBox="0 0 1200 855" role="img" aria-label="Round photo of a garden path leading to a red door through a pergola">
    <circle cx="1069" cy="248" r="75" fill="#ffffff"/>
    <circle cx="1069" cy="248" r="70" fill="#5a5f52"/>
  </svg>

  <!-- Intro -->
  <section class="intro">
    <h1 class="intro__title">LANDSCAPE CONSULTING AND DESIGN</h1>
    <h2 class="intro__subtitle">Landscaping to your Lifestyle</h2>
    <p>Owen Hartley, head of The Ridgewell Craft, offers a team that dedicates their efforts from concept development to installation and maintenance to ensure the outdoor creation becomes part of the client’s home and life experience with visual, tactile and sensory inclusions.</p>
    <p>Over its 20years, the business has developed a strong reputation for positive customer experiences, innovative designs and quality outcomes to suit individual needs and design styles.</p>
    <p>The Ridgewell Craft is a full-service landscaping and construction team that relish the journey to deliver high-end and bespoke outdoor designs.</p>
  </section>

  <!-- Services -->
  <section class="service" style="top:354px">
    <div class="service__head">
      <svg class="service__icon" viewBox="0 0 46 46" aria-hidden="true">
        <path d="M10 22a13 13 0 0 1 26 0z" fill="var(--green)"/>
        <rect x="7" y="21" width="32" height="4" rx="2" fill="var(--green)"/>
        <path d="M11 28h24v4a12 12 0 0 1-24 0z" fill="var(--green)"/>
        <path d="M30 34l10 8" stroke="var(--green-dark)" stroke-width="4" stroke-linecap="round"/>
      </svg>
      <h3 class="service__title">CONSTRUCTION</h3>
    </div>
    <ul class="service__list">
      <li><svg class="bullet" viewBox="0 0 14 14"><circle cx="7" cy="7" r="6" fill="none" stroke="var(--green)" stroke-width="1.5"/><path d="M5.5 4l3 3-3 3" fill="none" stroke="var(--green)" stroke-width="1.6"/></svg>Bespoke Structural Features</li>
      <li><svg class="bullet" viewBox="0 0 14 14"><circle cx="7" cy="7" r="6" fill="none" stroke="var(--green)" stroke-width="1.5"/><path d="M5.5 4l3 3-3 3" fill="none" stroke="var(--green)" stroke-width="1.6"/></svg>Water Features</li>
      <li><svg class="bullet" viewBox="0 0 14 14"><circle cx="7" cy="7" r="6" fill="none" stroke="var(--green)" stroke-width="1.5"/><path d="M5.5 4l3 3-3 3" fill="none" stroke="var(--green)" stroke-width="1.6"/></svg>Paving &amp; Pathways</li>
      <li><svg class="bullet" viewBox="0 0 14 14"><circle cx="7" cy="7" r="6" fill="none" stroke="var(--green)" stroke-width="1.5"/><path d="M5.5 4l3 3-3 3" fill="none" stroke="var(--green)" stroke-width="1.6"/></svg>Concreting and Aggregate</li>
    </ul>
  </section>

  <section class="service" style="top:548px">
    <div class="service__head">
      <svg class="service__icon" viewBox="0 0 46 46" aria-hidden="true">
        <circle cx="16" cy="14" r="10" fill="var(--green)"/>
        <circle cx="28" cy="20" r="11" fill="var(--green)"/>
        <circle cx="14" cy="26" r="8" fill="var(--green)"/>
        <rect x="19" y="26" width="5" height="16" fill="var(--green-dark)"/>
        <rect x="8" y="40" width="30" height="3" rx="1.5" fill="var(--green-dark)"/>
      </svg>
      <h3 class="service__title">GARDEN</h3>
    </div>
    <ul class="service__list">
      <li><svg class="bullet" viewBox="0 0 14 14"><circle cx="7" cy="7" r="6" fill="none" stroke="var(--green)" stroke-width="1.5"/><path d="M5.5 4l3 3-3 3" fill="none" stroke="var(--green)" stroke-width="1.6"/></svg>Plant &amp; Tree supply &amp; installation</li>
      <li><svg class="bullet" viewBox="0 0 14 14"><circle cx="7" cy="7" r="6" fill="none" stroke="var(--green)" stroke-width="1.5"/><path d="M5.5 4l3 3-3 3" fill="none" stroke="var(--green)" stroke-width="1.6"/></svg>Earth Preparation</li>
      <li><svg class="bullet" viewBox="0 0 14 14"><circle cx="7" cy="7" r="6" fill="none" stroke="var(--green)" stroke-width="1.5"/><path d="M5.5 4l3 3-3 3" fill="none" stroke="var(--green)" stroke-width="1.6"/></svg>Lawns</li>
      <li><svg class="bullet" viewBox="0 0 14 14"><circle cx="7" cy="7" r="6" fill="none" stroke="var(--green)" stroke-width="1.5"/><path d="M5.5 4l3 3-3 3" fill="none" stroke="var(--green)" stroke-width="1.6"/></svg>Irrigation Systems</li>
    </ul>
  </section>

  <section class="service" style="top:746px">
    <div class="service__head">
      <svg class="service__icon" viewBox="0 0 46 46" aria-hidden="true">
        <path d="M22 14c-2-6 2-10 8-10 0 6-3 9-8 10zM22 14c-1-5-5-7-10-6 1 5 5 7 10 6z" fill="var(--green)"/>
        <path d="M4 22h8l4 12h20l4-12z" fill="var(--green)"/>
        <circle cx="30" cy="39" r="4" fill="none" stroke="var(--green-dark)" stroke-width="2.5"/>
        <path d="M12 34l-4 6" stroke="var(--green-dark)" stroke-width="2.5"/>
      </svg>
      <h3 class="service__title">MAINTENANCE</h3>
    </div>
    <ul class="service__list">
      <li><svg class="bullet" viewBox="0 0 14 14"><circle cx="7" cy="7" r="6" fill="none" stroke="var(--green)" stroke-width="1.5"/><path d="M5.5 4l3 3-3 3" fill="none" stroke="var(--green)" stroke-width="1.6"/></svg>Garden &amp; Structural</li>
    </ul>
  </section>

  <!-- Process -->
  <section class="process">
    <h3 class="process__title">THE PROCESS</h3>
    <div class="process__step">
      <svg class="tick" viewBox="0 0 15 15"><circle cx="7.5" cy="7.5" r="6.5" fill="none" stroke="var(--green)" stroke-width="1.5"/><path d="M4.5 7.6l2 2 4-4" fill="none" stroke="var(--green)" stroke-width="1.7"/></svg>
      <p>TRC can work with an existing design or create a landscape design to suit your needs.</p>
    </div>
    <div class="process__step">
      <svg class="tick" viewBox="0 0 15 15"><circle cx="7.5" cy="7.5" r="6.5" fill="none" stroke="var(--green)" stroke-width="1.5"/><path d="M4.5 7.6l2 2 4-4" fill="none" stroke="var(--green)" stroke-width="1.7"/></svg>
      <p>Once a design has been established, Owen Hartley will go over your plans onsite and discuss the requirements to suit your space and climate and provide advice as needed.</p>
    </div>
    <div class="process__step">
      <svg class="tick" viewBox="0 0 15 15"><circle cx="7.5" cy="7.5" r="6.5" fill="none" stroke="var(--green)" stroke-width="1.5"/><path d="M4.5 7.6l2 2 4-4" fill="none" stroke="var(--green)" stroke-width="1.7"/></svg>
      <p>Owen will project-manage your entire outdoor construction and ensure you are updated throughout the journey.</p>
    </div>
    <div class="process__step">
      <svg class="tick" viewBox="0 0 15 15"><circle cx="7.5" cy="7.5" r="6.5" fill="none" stroke="var(--green)" stroke-width="1.5"/><path d="M4.5 7.6l2 2 4-4" fill="none" stroke="var(--green)" stroke-width="1.7"/></svg>
      <p>Our clients will experience honesty, integrity, and professionalism throughout the project which allows them to embrace their outdoor living after completion.</p>
    </div>
  </section>

  <!-- Brand and call -->
  <div class="brand">
    <div class="brand__name">The Ridgewell Craft</div>
    <div class="brand__division">PREMIER BRANCH</div>
  </div>
  <div class="callout">
    <span>CALL US TODAY</span>
    <svg viewBox="0 0 22 22" aria-hidden="true"><circle cx="11" cy="11" r="9.5" fill="none" stroke="var(--white)" stroke-width="1.8"/><path d="M7.5 6.5l2 0 1 2.6-1.3 1a6 6 0 0 0 3 3l1-1.3 2.6 1v2a1.2 1.2 0 0 1-1.3 1.1A9 9 0 0 1 6.4 7.8 1.2 1.2 0 0 1 7.5 6.5z" fill="var(--white)"/></svg>
    <span>0400 18 36 92</span>
  </div>

</main>
</body>
</html>
```